Corvane Health Web Page

We need a visually exciting webpage that introduces people to our practice. We are a practice that has both physiotherapy and psychology and we need the page to reflect this. We are also split across two practice locations. We need the page to be able to be updated regularly to include a blog spot and the linking in of our facebook page. There should be tabs to introduce our practitioners with some blurbs about them, a tab for people to be able to contact us, a tab to read about physiotherapy services and a tab to talk about psychology services. If there are other tabs than please include these. We are a practice that has treated world class athlete on a regular basis and see our selves as leaders in the field and the website must reflect this. I do not want basic clip-arty type things that anyone could have, we have to have something that draws people in.
Updates
Firstly, thanks everyone for their designs. I have attached some links to some physiotherapy websites that I think contain some interesting information and/or layout, as well as some comments,
Hi all,
Reason: Hi Guys,
We are so very close to finding a great design. I feel that we just need a bit of extra time to be able to clinch where we want to be. Thanks for your fantastic designs :)
Regards,
Martin and Ruth
Industry/Entity Type
Health
Requirements
Must have
- 2 Practice Addresses (details to follow for right applications)
Psychology aspect
Physiotherapy aspect
Ability to update blog

```html
<!DOCTYPE html>
<html lang="en">
<head>
<meta charset="utf-8">
<title>Corvane Health</title>
<link href="https://fonts.googleapis.com/css2?family=Open+Sans:ital,wght@0,300;0,400;0,600;0,700;1,400&display=swap" rel="stylesheet">
<style>
:root{
  --teal:#4ba3b9;
  --teal-dark:#3a8ea3;
  --heading:#4aa6c0;
  --orange:#f2652f;
  --orange-dark:#e0551f;
  --text:#555;
  --muted:#777;
  --icon:#b5b5b5;
  --panel:#ececec;
  --footer:#2c2e2f;
  --footer-bottom:#232425;
  --footer-text:#9a9a9a;
}
*{box-sizing:border-box;margin:0;padding:0}
html,body{width:1200px;height:2909px;overflow:hidden;background:#fff}
body{font-family:'Open Sans',Arial,sans-serif;color:var(--text);position:relative}
.abs{position:absolute}
/* header */
.brand{left:44px;top:18px;font-size:34px;font-weight:600;color:var(--teal)}
.brand-tag{left:44px;top:64px;font-size:14px;color:var(--muted)}
.socials{left:545px;top:22px;display:flex;gap:12px}
.socials span{width:48px;height:48px;border:2px solid #e2e2e2;border-radius:50%;display:flex;align-items:center;justify-content:center}
.phone-pill{left:966px;top:22px;width:186px;height:48px;border:2px solid #e2e2e2;border-radius:24px;font-size:17px;color:#aaa;display:flex;align-items:center;padding-left:48px}
.phone-pill svg{position:absolute;left:18px;top:12px}
.nav{left:32px;top:109px;width:1120px;height:49px;background:var(--teal);display:flex;align-items:center;padding-left:10px}
.nav a{color:#fff;font-size:15px;text-decoration:none;padding:0 25px}
.search{position:absolute;right:12px;top:9px;width:228px;height:31px;background:var(--teal-dark);color:#cfe6ec;font-size:14px;padding:6px 12px}
.search svg{position:absolute;right:10px;top:7px}
/* hero */
.hero{left:32px;top:158px;width:1120px;height:509px;background:linear-gradient(120deg,#dfe3e0 0%,#bfc5c2 40%,#c9b39f 65%,#e8e6e2 100%)}
.tabs{left:32px;top:667px;width:1120px;height:89px;display:flex;background:var(--orange)}
.tab{flex:1;padding:16px 0 0 22px;color:#fff;border-right:1px solid rgba(255,255,255,.35)}
.tab:last-child{border-right:0}
.tab.active{background:var(--orange-dark)}
.tab b{display:block;font-size:17px;font-weight:700}
.tab small{font-size:13px;display:block;margin-top:10px}
/* intro */
.intro-title{left:0;top:800px;width:1200px;text-align:center;font-size:37px;font-weight:300;color:var(--heading)}
.intro-sub{left:0;top:852px;width:1200px;text-align:center;font-size:20px;color:#666}
.services{left:32px;top:921px;width:1120px;display:flex;justify-content:space-between}
.service{width:224px;text-align:center}
.service .ring{width:128px;height:128px;border:3px solid #d5d5d5;border-radius:50%;margin:0 auto;display:flex;align-items:center;justify-content:center}
.service h3{font-size:19px;font-weight:700;color:#333;margin-top:28px}
.service p{font-size:14.5px;color:#666;line-height:1.6;margin-top:10px}
.divider{left:32px;top:1229px;width:1120px;height:2px;background:#e6e6e6}
/* doctors */
.h2{font-size:35px;font-weight:300;color:var(--heading)}
.lede{font-size:14.5px;color:#666;line-height:1.55}
.doctors-title{left:32px;top:1298px}
.doctors-lede{left:32px;top:1350px;width:750px}
.doctor{top:1416px;width:230px}
.doctor h4{font-size:18px;font-weight:700;color:#333}
.doctor .photo{margin-top:20px;width:230px;height:176px;border:5px solid #e3e3e3;position:relative;background:linear-gradient(160deg,#e9ecee,#c8cfd3)}
.doctor .photo em{position:absolute;right:0;bottom:0;background:rgba(90,90,90,.85);color:#fff;font-style:normal;font-size:13px;padding:6px 14px}
.doctor p{margin-top:26px;font-size:14px;line-height:1.65;color:#666}
.btn{background:var(--orange);color:#fff;font-size:14.5px;display:inline-block;padding:9px 17px}
.more-docs{left:32px;top:1789px}
/* testimonials */
.say-title{left:32px;top:1895px}
.say-lede{left:32px;top:1946px;width:750px}
.avatar{left:32px;top:2031px;width:90px;height:90px;border-radius:50%;background:linear-gradient(160deg,#cfd6db,#8d9aa3)}
.quote{left:148px;top:2024px;width:640px;font-style:italic;font-size:18px;line-height:1.6;color:#555}
.cite{left:148px;top:2130px;font-size:15px;color:#555}
.cite span{color:var(--orange)}
.arrows{left:146px;top:2182px;display:flex;gap:4px}
.arrows i{width:22px;height:22px;background:#e1e1e1;display:flex;align-items:center;justify-content:center}
/* appointment */
.appt{left:800px;top:1297px;width:352px;height:654px;background:var(--panel)}
.appt-head{height:157px;background:linear-gradient(#62b4c8,var(--teal-dark));color:#fff;padding:18px 25px}
.appt-head h3{font-size:26px;font-weight:400}
.appt-head .num{font-size:31px;margin-top:16px;padding-left:42px;position:relative}
.appt-head .num svg{position:absolute;left:0;top:6px}
.or{position:absolute;left:152px;top:141px;width:40px;height:30px;border-radius:15px;background:var(--orange);color:#fff;font-size:13px;text-align:center;line-height:30px}
.field{position:absolute;left:36px;width:278px;height:40px;background:#fff;border:1px solid #d6d6d6;font-size:14px;color:#999;padding:10px 12px}
.captcha{position:absolute;left:36px;top:514px;width:112px;height:40px;background:#fff;border:1px solid #d6d6d6;color:var(--orange);font-size:25px;padding:0 10px;line-height:38px}
.captcha-in{position:absolute;left:162px;top:514px;width:80px;height:40px;background:#fff;border:1px solid #d6d6d6}
.submit{position:absolute;left:36px;top:582px;padding:9px 16px}
/* newsletter */
.news-title{left:800px;top:2004px;font-size:30px;font-weight:300;color:var(--heading)}
.news{left:800px;top:2060px;width:352px;height:129px;background:var(--panel);padding:22px 25px}
.news p{font-size:14px;color:#777}
.news .email{position:absolute;left:25px;top:62px;width:188px;height:40px;background:#fff;border:1px solid #d6d6d6;font-size:14px;color:#999;padding:10px 12px}
.news .go{position:absolute;left:227px;top:62px;padding:10px 15px}
/* footer */
.footer{left:0;top:2291px;width:1200px;height:569px;background:var(--footer)}
.f-col{top:2355px;width:260px;color:var(--footer-text)}
.f-col h5{font-size:27px;font-weight:300;color:#e8e8e8;margin-bottom:26px}
.f-col p{font-size:14px;line-height:1.65;color:#767676}
.f-col ul{list-style:none}
.f-col li{font-size:14.5px;color:#cfcfcf;line-height:30px}
.f-col li:before{content:"\2022";color:#888;margin-right:10px}
.post{display:flex;gap:16px;padding-bottom:18px;margin-bottom:18px;border-bottom:1px dashed #555}
.post .thumb{width:60px;height:40px;flex:none;background:linear-gradient(135deg,#8fb4c3,#d9d1bf)}
.post b{display:block;font-weight:400;font-size:14.5px;color:#e8e8e8;line-height:1.45}
.post i{font-size:12.5px;color:#bdbdbd}
.map{width:300px;height:158px;background:linear-gradient(135deg,#ece9e2,#d8d3c7)}
.loc p{font-size:14px;color:#bdbdbd;margin-top:14px;line-height:1.5}
.loc p b{font-weight:600;color:#fff}
.f-bottom{left:0;top:2860px;width:1200px;height:49px;background:var(--footer-bottom);font-size:13.5px;color:#9a9a9a;display:flex;justify-content:space-between;align-items:center;padding:0 32px}
</style>
</head>
<body>

<header>
  <div class="abs brand">Corvane Health</div>
  <div class="abs brand-tag">Menus colors will be set to match the logo</div>
  <div class="abs socials" aria-label="Share and follow links">
    <span><svg width="20" height="20" viewBox="0 0 20 20" fill="none" stroke="var(--icon)" stroke-width="2"><circle cx="5" cy="10" r="2.5"/><circle cx="15" cy="4" r="2.5"/><circle cx="15" cy="16" r="2.5"/><path d="M7 9l6-4M7 11l6 4"/></svg></span>
    <span><svg width="20" height="20" viewBox="0 0 20 20" fill="none" stroke="var(--icon)" stroke-width="2"><path d="M3 4h14v9H8l-4 3v-3H3z" stroke-linejoin="round"/></svg></span>
    <span><svg width="20" height="20" viewBox="0 0 20 20" fill="none" stroke="var(--icon)" stroke-width="2"><rect x="2" y="4" width="16" height="12" rx="1"/><path d="M2 5l8 6 8-6"/></svg></span>
    <span><svg width="20" height="20" viewBox="0 0 20 20"><rect x="2" y="4" width="16" height="12" rx="3" fill="var(--icon)"/><path d="M8 7v6l5-3z" fill="#fff"/></svg></span>
    <span><svg width="20" height="20" viewBox="0 0 20 20" fill="none" stroke="var(--icon)" stroke-width="2"><circle cx="10" cy="10" r="7.5"/><path d="M2.5 10h15M10 2.5c-3 3.5-3 11.5 0 15M10 2.5c3 3.5 3 11.5 0 15"/></svg></span>
    <span><svg width="20" height="20" viewBox="0 0 20 20" fill="none" stroke="var(--icon)" stroke-width="2"><circle cx="10" cy="6.5" r="3.5"/><path d="M3 18c0-4 3-6.5 7-6.5s7 2.5 7 6.5"/></svg></span>
    <span><svg width="20" height="20" viewBox="0 0 20 20" fill="none" stroke="var(--icon)" stroke-width="2.2"><circle cx="4.5" cy="15.5" r="1.6" fill="var(--icon)" stroke="none"/><path d="M3 9a8 8 0 0 1 8 8M3 3a14 14 0 0 1 14 14"/></svg></span>
  </div>
  <div class="abs phone-pill">
    <svg width="16" height="24" viewBox="0 0 16 24"><rect x="1" y="1" width="14" height="22" rx="3" fill="none" stroke="#bbb" stroke-width="2"/><circle cx="8" cy="18" r="1.6" fill="#bbb"/></svg>
    1888-888-8888
  </div>
  <nav class="abs nav">
    <a>Home</a><a>Blog</a><a>Doctors</a><a>Services</a><a>Gallery</a><a>FAQs</a><a>Features</a><a>Contact Us</a>
    <div class="search">Search
      <svg width="18" height="18" viewBox="0 0 18 18"><circle cx="7.5" cy="7.5" r="5.5" fill="none" stroke="#fff" stroke-width="2.2"/><line x1="11.5" y1="11.5" x2="16.5" y2="16.5" stroke="#fff" stroke-width="2.6"/></svg>
    </div>
  </nav>
</header>

<section>
  <div class="abs hero" role="img" aria-label="Physiotherapist treating a patient's shoulder in a bright clinic room"></div>
  <div class="abs tabs">
    <div class="tab active"><b>Physiotherapy Tab1</b><small>Lorem ipsum dolor sit amet</small></div>
    <div class="tab"><b>Physiotherapy Tab2</b><small>Lorem ipsum dolor sit amet</small></div>
    <div class="tab"><b>Physiotherapy Tab3</b><small>Lorem ipsum dolor sit amet</small></div>
    <div class="tab"><b>Physiotherapy Tab4</b><small>Lorem ipsum dolor sit amet</small></div>
    <div class="tab"><b>Our Doctors</b><small>Meet our doctors</small></div>
  </div>
</section>

<section>
  <h1 class="abs intro-title">Leaders in Physiotherapy and Psychology Care</h1>
  <p class="abs intro-sub">Trusted by everyday patients and world class athletes</p>
  <div class="abs services">
    <div class="service">
      <div class="ring"><svg width="56" height="56" viewBox="0 0 56 56" fill="none" stroke="#bbb" stroke-width="4"><rect x="6" y="16" width="44" height="32" rx="4"/><path d="M20 6l8 10 8-10"/></svg></div>
      <h3>Service #1</h3><p>Lorem ipsum dolor sit amet, consectetuer adipiscing elit.</p>
    </div>
    <div class="service">
      <div class="ring"><svg width="56" height="56" viewBox="0 0 56 56"><path d="M4 28C12 14 44 14 52 28 44 42 12 42 4 28z" fill="#bbb"/><circle cx="28" cy="28" r="9" fill="#fff"/><circle cx="28" cy="28" r="4" fill="#bbb"/></svg></div>
      <h3>Service #2</h3><p>Lorem ipsum dolor sit amet, consectetuer adipiscing elit.</p>
    </div>
    <div class="service">
      <div class="ring"><svg width="56" height="56" viewBox="0 0 56 56"><rect x="20" y="6" width="16" height="8" fill="none" stroke="#bbb" stroke-width="4"/><rect x="6" y="14" width="44" height="34" rx="4" fill="#bbb"/><path d="M28 20v22M17 31h22" stroke="#fff" stroke-width="7"/></svg></div>
      <h3>Rehabilitation Center</h3><p>Lorem ipsum dolor sit amet, consectetuer adipiscing elit.</p>
    </div>
    <div class="service">
      <div class="ring"><svg width="56" height="56" viewBox="0 0 56 56"><path d="M14 6l8 10-5 6c3 7 9 13 16 16l6-5 10 8-6 8C25 50 6 31 6 12z" fill="none" stroke="#bbb" stroke-width="4" stroke-linejoin="round"/></svg></div>
      <h3>Service #4</h3><p>Lorem ipsum dolor sit amet, consectetuer adipiscing elit.</p>
    </div>
    <div class="service">
      <div class="ring"><svg width="56" height="56" viewBox="0 0 56 56"><path d="M28 6C22 18 16 26 16 35a12 12 0 0 0 24 0C40 26 34 18 28 6z" fill="#bbb"/></svg></div>
      <h3>Service #5</h3><p>Lorem ipsum dolor sit amet, consectetuer adipiscing elit.</p>
    </div>
  </div>
  <div class="abs divider"></div>
</section>

<section>
  <h2 class="abs h2 doctors-title">Meet Our Doctors</h2>
  <p class="abs lede doctors-lede">Lorem ipsum dolor sit amet, consectetuer adipiscing elit, sed diam nonummy nibh euismod tincidunt ut laoreet dolore magna aliquam erat volutpat.</p>
  <div class="abs doctor" style="left:32px">
    <h4>Dr.Elsa Morrow</h4>
    <div class="photo" role="img" aria-label="Portrait of a psychologist"><em>Psychology</em></div>
    <p>Eastbrook Clinic June 2009 to July 2010 Lorem ipsum dolor sit amet, consectetur adipiscing elit, sed do...</p>
  </div>
  <div class="abs doctor" style="left:286px">
    <h4>Dr.Nadia Fenwick</h4>
    <div class="photo" role="img" aria-label="Portrait of a psychologist"><em>Psychology</em></div>
    <p>Eastbrook Clinic June 2009 to July 2010 Lorem ipsum dolor sit amet, consectetur adipiscing elit, sed do...</p>
  </div>
  <div class="abs doctor" style="left:543px">
    <h4>Dr. Peter Holm</h4>
    <div class="photo" role="img" aria-label="Portrait of a physiotherapist"><em>Physiotherapy</em></div>
    <p>Eastbrook Clinic June 2009 to July 2010 Lorem ipsum dolor sit amet, consectetur adipiscing elit, sed do...</p>
  </div>
  <div class="abs btn more-docs">More Doctors</div>

  <h2 class="abs h2 say-title">What our patients say</h2>
  <p class="abs lede say-lede">Lorem ipsum dolor sit amet, consectetuer adipiscing elit, sed diam nonummy nibh euismod tincidunt ut laoreet dolore magna aliquam erat volutpat.</p>
  <div class="abs avatar" role="img" aria-label="Patient portrait"></div>
  <blockquote class="abs quote">Lorem ipsum dolor sit amet, consectetuer adipiscing elit, sed diam nonummy nibh euismod tincidunt ut laoreet dolore magna aliquam erat volutpat. Ut wisi enim ad minim veniam, quis nostrud exerci tation ullamcorper.</blockquote>
  <div class="abs cite"><span>Owen Tate</span>, Dental Care</div>
  <div class="abs arrows">
    <i><svg width="8" height="10" viewBox="0 0 8 10"><path d="M7 0L1 5l6 5z" fill="#666"/></svg></i>
    <i><svg width="8" height="10" viewBox="0 0 8 10"><path d="M1 0l6 5-6 5z" fill="#666"/></svg></i>
  </div>
</section>

<aside>
  <div class="abs appt">
    <div class="appt-head">
      <h3>Make an Appointment</h3>
      <div class="num"><svg width="22" height="28" viewBox="0 0 22 28"><rect x="1" y="1" width="20" height="26" rx="4" fill="#fff"/><rect x="5" y="5" width="12" height="14" fill="#3a8ea3"/><circle cx="11" cy="23" r="1.8" fill="#3a8ea3"/></svg>1-800-123-4567</div>
    </div>
    <div class="or">OR</div>
    <div class="field" style="top:187px">Full Name</div>
    <div class="field" style="top:242px">Phone Number</div>
    <div class="field" style="top:297px">Email Address</div>
    <div class="field" style="top:352px">Appointment Date</div>
    <div class="field" style="top:407px;height:92px">Message</div>
    <div class="captcha">ofeix</div>
    <div class="captcha-in"></div>
    <div class="btn submit">Submit Request</div>
  </div>
  <h3 class="abs news-title">Newsletter</h3>
  <div class="abs news">
    <p>Sign up our newsletter to get latest updates</p>
    <div class="email">Email Address</div>
    <div class="btn go">Go</div>
  </div>
</aside>

<footer>
  <div class="abs footer"></div>
  <div class="abs f-col" style="left:32px">
    <h5>About us goes here</h5>
    <p>Lorem ipsum dolor sit amet, consectetuer adipiscing elit. Duis adipiscing id nulla vel lorem dapibus fringilla eget non felis, porttitor lectus.</p>
  </div>
  <div class="abs f-col" style="left:320px">
    <h5>Quick Links</h5>
    <ul><li>Home</li><li>Blog</li><li>Services</li><li>Doctors</li><li>Contact Us</li></ul>
  </div>
  <div class="abs f-col" style="left:606px;width:252px">
    <h5>Recent Posts</h5>
    <div class="post"><div class="thumb" role="img" aria-label="Post thumbnail"></div><div><b>Latest Health Lessons</b><i>September 25, 2012</i></div></div>
    <div class="post"><div class="thumb" role="img" aria-label="Post thumbnail"></div><div><b>The Benefits of Middle-Age Fitness</b><i>September 25, 2012</i></div></div>
    <div class="post"><div class="thumb" role="img" aria-label="Post thumbnail"></div><div><b>For Young Athletes, Good Reasons to Break the Fast-Food Habit</b><i>September 25, 2012</i></div></div>
  </div>
  <div class="abs f-col loc" style="left:894px;width:300px">
    <h5>Our Locations</h5>
    <div class="map" role="img" aria-label="Street map showing both practice locations"></div>
    <p>Harlow Care Center, Suite 12345<br>Brindle Medical Suites, Unit 8</p>
    <p><b>Ph:</b> 800 123 4567</p>
    <p><b>Email:</b> info@corvanehealth.example</p>
  </div>
  <div class="abs f-bottom"><span>© copyright 2014 - all rights are reserved.</span><span>Text on the right side of footer.</span></div>
</footer>

</body>
</html>
```